Advertising flyer for proofreading business.

Hello everyone,

I need an advertising flyer for a new proofreading company in Australia.

I would like your design in be in two sizes:
- A4 (to be posted on noticeboards),
- A6 (to be printed in larger quantity to give away)
(please see the size specification file attached).

The text file is attached (Ad Text) and it contains lots of information. Please feel free to include your choice of text from the text file, but please include Poster title, and highlight 'ESL' and students discounts.

I understand that it is impossible to include the same amount of information on A6 and A4, so please feel free to chose what fits on each of them, but please keep the design similar.

I have attached our company logo, but feel free to adjust it to the poster design (feel free to change the color as well). The original logo file contains circle around it, please feel free to remove it and include only the typeset as it can be seen here: http://www.lexmarka.com.au/.

Flyers will be printed, so please see the specification file for details.

I will do my best to respond to feedback as soon as possible.

I appreciate your participation, time and help,
Best wishes,
Bartosz

Target Market(s)

Students, authors

Industry/Entity Type

Business

Colors

Designer to choose colors to be used in the design.

Requirements
Must have
• It would be good if poster is easy to spot on busy noticeboards and attract attention.
• Please keep the poster in the positive/optimistic mood, and so that it focuses on students, maybe photos of graduates(?).
• Poster title,
• Please include the list of proof-read documents as they are described in the attached text file (Ad Text).
• Please highlight students discounts and ESL.
Nice to have
• I would like to leave the creative freedom to all designers so at this point I have not adjusted the Look and Feel sliders. Please feel free to offer your own take on this.
• It would be nice if most of the text could be fit to the poster.

```html
<!DOCTYPE html>
<html lang="en">
<head>
<meta charset="utf-8">
<title>Lexmarka – Professional English Language Proofreading</title>
<link rel="stylesheet" href="https://fonts.googleapis.com/css2?family=Montserrat:wght@700;800&family=Open+Sans:ital,wght@0,400;0,600;0,700;1,400&display=swap">
<style>
  :root {
    --navy: #132c3a;
    --teal: #1a8a8c;
    --teal-bright: #2bb3b0;
    --teal-deep: rgba(18, 92, 98, 0.88);
    --band: rgba(16, 38, 46, 0.94);
    --white: #ffffff;
    --sky-top: #e4f0f4;
    --sky-mid: #a9c6d3;
    --crowd: #56707c;
    --gown: #18212b;
  }
  * { margin: 0; padding: 0; box-sizing: border-box; }
  html, body { width: 849px; height: 1200px; overflow: hidden; background: var(--white); }
  .flyer {
    position: relative; width: 849px; height: 1200px; overflow: hidden;
    font-family: "Open Sans", Arial, sans-serif; color: var(--navy); background: var(--white);
  }
  .pattern {
    position: absolute; top: 0; right: 0; width: 480px; height: 240px;
    background: linear-gradient(215deg, var(--teal) 0%, rgba(43,179,176,0.45) 35%, rgba(255,255,255,0) 72%);
  }
  .photo {
    position: absolute; left: 0; top: 395px; width: 849px; height: 805px;
    background:
      radial-gradient(ellipse 60% 30% at 30% 62%, rgba(220,200,180,0.35), transparent 70%),
      radial-gradient(ellipse 50% 25% at 80% 60%, rgba(220,200,180,0.3), transparent 70%),
      linear-gradient(180deg, var(--white) 0%, var(--sky-top) 10%, var(--sky-mid) 30%, var(--crowd) 50%, #2a3744 65%, var(--gown) 100%);
  }
  .title {
    position: absolute; top: 28px; left: 0; width: 849px; text-align: center;
    font-family: "Montserrat", Arial, sans-serif; font-weight: 800;
    font-size: 73px; line-height: 1.1; letter-spacing: -0.5px; color: var(--navy);
  }
  .intro {
    position: absolute; top: 282px; left: 20px; width: 809px; text-align: center;
    font-size: 17.5px; line-height: 1.45; color: var(--navy);
  }
  .intro strong { font-weight: 700; font-size: 18.5px; }
  .services {
    position: absolute; top: 415px; left: 34px; width: 380px;
    font-size: 15px; line-height: 1.5; color: var(--teal);
  }
  .services h2 { font-size: 15px; font-weight: 700; color: var(--navy); margin-bottom: 2px; }
  .price-box {
    position: absolute; top: 505px; left: 420px; width: 415px; height: 222px;
    background: var(--teal-deep); color: var(--white);
    padding: 14px 18px; text-align: center; font-size: 13.5px; line-height: 1.35;
  }
  .price-box h2 {
    font-family: "Montserrat", Arial, sans-serif; font-weight: 700; font-size: 21px;
    color: var(--teal-bright); margin-bottom: 6px; letter-spacing: 0.5px; text-align: left;
  }
  .price-box p { margin-bottom: 5px; }
  .price-box .small { font-size: 12px; }
  .contact-band {
    position: absolute; left: 0; top: 895px; width: 849px; height: 305px; background: var(--band);
  }
  .brand {
    position: absolute; top: 920px; left: 34px; display: flex; align-items: center; gap: 12px;
    font-family: "Montserrat", Arial, sans-serif; font-weight: 700; font-size: 52px; color: var(--white);
  }
  .brand-dot { width: 30px; height: 30px; border-radius: 50%; background: var(--teal-bright); }
  .contact {
    position: absolute; top: 1040px; left: 34px; width: 360px;
    font-size: 14px; line-height: 1.45; color: var(--white);
  }
  .contact .name { font-weight: 700; }
  .contact .lead { margin-top: 14px; }
  .contact a { color: var(--teal-bright); text-decoration: none; font-weight: 600; }
  .testimonial {
    position: absolute; top: 962px; left: 455px; width: 340px;
    font-size: 16.5px; line-height: 1.45; color: var(--white); font-style: italic; text-align: center;
  }
  .quote-mark {
    position: absolute; font-family: "Montserrat", Arial, sans-serif; font-size: 90px;
    font-weight: 800; color: var(--teal-bright); line-height: 1;
  }
  .quote-open { top: 945px; left: 400px; }
  .quote-close { top: 1090px; left: 765px; }
</style>
</head>
<body>
<div class="flyer">
  <div class="pattern" role="img" aria-label="Decorative teal triangle pattern"></div>
  <div class="photo" role="img" aria-label="Photo of happy graduates in gowns tossing their caps"></div>

  <h1 class="title">PROFESSIONAL,<br>ENGLISH LANGUAGE<br>PROOFREADING.</h1>

  <div class="intro">
    <p>Help with English as a second language (ESL)</p>
    <p><strong>Proofreading by a native English speaker with an English Honours degree.</strong></p>
    <p>Includes correct all English language errors, spelling and grammar mistakes,<br>reference checking and editing for style, coherence and clarity.</p>
  </div>

  <section class="services">
    <h2>WE WILL PROOFREAD YOUR:</h2>
    <p>essays &amp; assignments | theses | resumes<br>business correspondence | training manuals<br>newsletters | advertising copy | brochures,<br>catalogues &amp; media releases | websites<br>presentations &amp; speeches<br>novels &amp; short stories</p>
  </section>

  <section class="price-box">
    <h2>PRICE GUIDE</h2>
    <p>Prices start at only $20 (short memos, flyers, letters).</p>
    <p>Discounts for not-for-profit organisations and students.</p>
    <p>Great student discount rate: $25 per hour<br><span class="small">(roughly 1000 words - 4 pages - of well-written text).</span></p>
    <p>Package deals on documents over 50,000 words.</p>
    <p>Fast, negotiable time-frames<br><span class="small">(same day service available by special arrangement).</span></p>
  </section>

  <div class="contact-band"></div>

  <div class="brand"><span class="brand-dot"></span>Lexmarka</div>

  <div class="contact">
    <p class="name">Dana Corvell</p>
    <p>Operations Manager</p>
    <p>corvellAU</p>
    <p class="lead">Contact us for an obligation-free quote:</p>
    <p><a href="tel:0400123456">0400 123 456</a> / <a href="mailto:proofing@lexmarka.com.au">proofing@lexmarka.com.au</a></p>
  </div>

  <span class="quote-mark quote-open">“</span>
  <blockquote class="testimonial">Erin understood our requirements quickly and has been fantastic at delivering quality work, on time and within agreed budget. It's a pleasure to work with her.</blockquote>
  <span class="quote-mark quote-close">”</span>
</div>
</body>
</html>
```